Porchlight To Bin Co Valet Trash Recycling

I want to create a colorful brochure, I really like my company colors, with basic information about valet trash for apartment complexes. You can include some apartment recycling information as well, but 80% trash, 20% recycling. I have included my logo in the attachments. Also, you can find information at porchlighttobinco.example, very basic and I will be redoing my website as well.

many people are giving information about business and residential recycling, I only want information on trash and recycling valet for apartments

Target Market(s)

apartment complex tenants and management

Industry/Entity Type

Apartment

Number of Pages Required

4 page

Font styles to use
Serif
Sans Serif

Colors
9bcb3b
f37122
0355a3

Requirements
Must have
• Tri-Fold brochure, colorful, well organized. Advantages for tenants and for property management.

```html
<!DOCTYPE html>
<html lang="en">
<head>
<meta charset="utf-8">
<title>Porchlight To Bin Co — Valet Trash Tri-Fold</title>
<link rel="stylesheet" href="https://fonts.googleapis.com/css2?family=Arimo:wght@400;700&family=Roboto+Condensed:wght@700&family=Tinos:wght@400;700&display=swap">
<style>
  :root {
    --orange: #e8601c;
    --orange-light: #f37122;
    --green: #6fb32e;
    --green-light: #9bcb3b;
    --blue: #0355a3;
    --ink: #1a1a1a;
    --charcoal: #3a3a3a;
    --paper: #ffffff;
    --backdrop: #e4e4e4;
    --sans: "Arimo", Arial, sans-serif;
    --condensed: "Roboto Condensed", "Arial Narrow", sans-serif;
    --serif: "Tinos", "Times New Roman", serif;
  }
  * { box-sizing: border-box; margin: 0; padding: 0; }
  html, body { width: 1200px; height: 907px; overflow: hidden; }
  body { background: var(--backdrop); font-family: var(--sans); position: relative; }

  .brochure {
    position: absolute; left: 100px; top: 95px;
    width: 1003px; height: 713px;
    background: var(--paper); overflow: hidden;
    box-shadow: 0 6px 18px rgba(0,0,0,.25);
  }
  .layer { position: absolute; inset: 0; }

  /* ---------- outer-left panel ---------- */
  .panel-about {
    position: absolute; left: 0; top: 270px; width: 340px; height: 395px;
    background: linear-gradient(180deg, var(--orange) 0%, var(--orange-light) 60%, var(--orange) 100%);
    color: #fff; padding: 16px 18px 0;
  }
  .section-title {
    font-family: var(--serif); font-weight: 700; text-transform: uppercase;
    font-size: 17px; line-height: 1.1; text-align: center; letter-spacing: .3px; margin-bottom: 5px;
  }
  .body-copy { font-size: 10.3px; line-height: 1.22; text-align: justify; }
  .section-title.services { margin-top: 7px; }
  .tagline {
    position: absolute; left: 0; top: 292px; width: 340px;
    font-family: var(--sans); font-weight: 700; text-align: center;
    font-size: 15.5px; line-height: 1.4;
  }
  .tagline .big { font-size: 19.5px; display: block; }
  .phone-large {
    position: absolute; left: 0; top: 352px; width: 340px;
    font-family: var(--condensed); font-weight: 700; color: var(--ink);
    font-size: 36px; line-height: 1; text-align: center; letter-spacing: .5px;
  }
  .footer-left {
    position: absolute; left: 0; top: 665px; width: 340px; height: 48px;
    background: var(--ink); color: #fff; text-align: center;
    font-size: 11px; line-height: 17px; padding-top: 7px;
  }

  /* ---------- middle panel ---------- */
  .panel-contact {
    position: absolute; left: 340px; top: 0; width: 330px; height: 713px;
    background: linear-gradient(180deg, #ffffff 0%, #f1f3ef 60%, #e9ede4 100%);
  }
  .wordmark {
    font-family: var(--sans); font-weight: 400; color: var(--blue);
    display: flex; align-items: center; gap: 7px; white-space: nowrap;
  }
  .wordmark .dot { width: 13px; height: 13px; border-radius: 50%; background: var(--orange); flex: none; }
  .brand-url { font-size: 8px; color: var(--orange); }
  .contact-block { position: absolute; left: 0; width: 330px; top: 148px; text-align: center; }
  .contact-block .wordmark { font-size: 17px; justify-content: center; }
  .contact-block .brand-url { margin: 1px 0 10px 40px; }
  .contact-name { font-weight: 700; color: var(--orange); font-size: 12.5px; margin-bottom: 2px; }
  .contact-line { font-size: 11.5px; line-height: 15.5px; color: var(--ink); }
  .contact-line.gap { margin-top: 6px; }
  .contact-line.bold { font-weight: 700; }
  .partner-badge {
    position: absolute; left: 106px; top: 305px; width: 130px; height: 68px;
    background: var(--green); border-radius: 4px;
  }
  .photo-couple {
    position: absolute; left: 355px; top: 395px; width: 268px; height: 318px;
    background: radial-gradient(ellipse at 50% 45%, #c9d7e6 0%, #8fa6c2 55%, #556d8a 100%);
    border-radius: 120px 120px 0 0;
  }

  /* ---------- outer-right panel ---------- */
  .panel-cover { position: absolute; left: 670px; top: 0; width: 333px; height: 713px; }
  .cover-brand { position: absolute; left: 25px; top: 26px; }
  .cover-brand .wordmark { font-size: 20px; }
  .cover-brand .brand-url { text-align: right; margin-top: 2px; }
  .stripe { position: absolute; left: 0; width: 333px; }
  .stripe.green { top: 92px; height: 12px; background: var(--green); }
  .stripe.charcoal { top: 110px; height: 8px; background: var(--charcoal); }
  .stripe.orange { top: 122px; height: 8px; background: var(--orange); }
  .photo-beach {
    position: absolute; left: 0; top: 130px; width: 333px; height: 242px;
    background: linear-gradient(180deg, #dfe6ec 0%, #b9c9d2 38%, #8f8470 62%, #6f6452 100%);
  }
  .cover-copy { position: absolute; left: 0; top: 395px; width: 333px; height: 270px; color: #fff; text-align: center; }
  .headline-small { font-family: var(--condensed); font-weight: 700; font-size: 19px; color: #fff; margin-top: 38px; letter-spacing: .2px; }
  .headline-large { font-family: var(--condensed); font-weight: 700; font-size: 41px; line-height: 1; margin-top: 2px; }
  .headline-city { font-family: var(--serif); font-weight: 700; font-size: 21px; color: var(--ink); margin-top: 22px; letter-spacing: .4px; }
  .cover-intro {
    margin: 18px 12px 0; padding: 12px 14px;
    background: rgba(255,255,255,.12);
    font-family: var(--serif); font-size: 11.4px; line-height: 1.3; text-align: justify;
  }
  .footer-right {
    position: absolute; left: 0; top: 665px; width: 333px; height: 48px;
    background: var(--ink); color: #fff; text-align: center;
    font-size: 11.5px; letter-spacing: 3px; line-height: 48px;
  }
</style>
</head>
<body>
  <main class="brochure">

    <section class="panel-contact">
      <div class="contact-block">
        <div class="wordmark"><span class="dot"></span>Porchlight To Bin Co</div>
        <div class="brand-url">porchlighttobinco.example</div>
        <p class="contact-name">Marcus Delane</p>
        <p class="contact-line">4820 Larkspur Ave #118</p>
        <p class="contact-line">Pinebrook, TX 77490</p>
        <p class="contact-line gap">409-555-0186</p>
        <p class="contact-line gap bold">hello@porchlighttobinco.example</p>
      </div>
      <div class="partner-badge" role="img" aria-label="Partner hauler badge"></div>
    </section>

    <svg class="layer" width="1003" height="713" viewBox="0 0 1003 713" aria-hidden="true">
      <polygon points="690,395 1003,395 1003,665 600,665" fill="#6fb32e"/>
      <polyline points="700,382 1003,382" stroke="#e8601c" stroke-width="8" fill="none"/>
      <line x1="692" y1="384" x2="596" y2="665" stroke="#e8601c" stroke-width="8"/>
    </svg>

    <div class="photo-couple" role="img" aria-label="Smiling young couple holding a clear recycling bin with plastic bottles"></div>

    <svg class="layer" width="1003" height="713" viewBox="0 0 1003 713">
      <polygon points="0,0 410,0 272,262 0,262" fill="#7a756e" role="img" aria-label="Worker in orange uniform and hard hat loading plastic waste into a bin on a city street"/>
      <polyline points="418,0 278,268 0,268" stroke="#6fb32e" stroke-width="6" fill="none"/>
    </svg>

    <section class="panel-about">
      <h2 class="section-title">About the Company</h2>
      <p class="body-copy">Porchlight To Bin Co (PTB) is a Houston-based business created by Marcus Delane, a Bayou City University student and professional mixed martial artist. Marcus previously owned and operated the successful trash removal service, Marcus's Curbside, while he was a high school student-athlete in Galveston. He has now founded a similar service in the Houston area. Marcus plans to keep PTB ahead of its competitors by focusing on customer satisfaction, technology, efficiency, and professionalism. PTB is fully insured; proof of insurance will be provided upon request. Testimonials from former clients reveal so much about how a company operates and performs. We are happy to provide references upon request.</p>
      <h2 class="section-title services">PTB Services</h2>
      <p class="body-copy">Porchlight To Bin Co (PTB) is a complete trash and recycling valet service designed to keep apartment complexes and its units clean, make complexes more environmentally friendly, and to keep tenants satisfied.</p>
      <p class="tagline">Keeping Apartment Complexes Cleaner<span class="big">and Greener Across Houston</span></p>
      <p class="phone-large">409-555-0186</p>
    </section>
    <footer class="footer-left">
      <div>porchlighttobinco.example</div>
      <div>hello@porchlighttobinco.example</div>
    </footer>

    <section class="panel-cover">
      <div class="cover-brand">
        <div class="wordmark"><span class="dot"></span>Porchlight To Bin Co</div>
        <div class="brand-url">porchlighttobinco.example</div>
      </div>
      <div class="stripe green"></div>
      <div class="stripe charcoal"></div>
      <div class="stripe orange"></div>
      <div class="photo-beach" role="img" aria-label="Volunteer in orange top collecting plastic litter on a beach"></div>
      <div class="cover-copy">
        <p class="headline-small">FULL-SERVICE WASTE REMOVAL</p>
        <h1 class="headline-large">AND RECYCLING</h1>
        <p class="headline-city">HOUSTON, TEXAS</p>
        <p class="cover-intro">Taking out somebody's trash is a timeless gesture of kindness. Porchlight To Bin Co (PTB) takes that act of kindness one step further: your tenants will never again have to bother with trash past their own doorsteps!</p>
      </div>
      <footer class="footer-right">porchlighttobinco.example</footer>
    </section>

  </main>
</body>
</html>
```